Cozy Sprouts Business Cards

I need a business card for my new Company called Cozy Sprouts. We create handmade baby moccasins, headbands, t-shirts and more. I want some that will appeal to parents, and to go with the colors of my logo that I have attached. feel free to be creative. I would like my logo placed somewhere on the card.

Industry/Entity Type

Retail

Contact Information for Business Card

Cozy Sprouts
24816 Maplecrest D #5172
Brenwick Or 97318
Rosalind Vantrey Ceo
Info@Cozy-Sprouts.com
www.Cozy-Sprouts.com
Phone 5415817320

Requirements
Nice to have
• Logo included

```html
<!DOCTYPE html>
<html lang="en">
<head>
<meta charset="utf-8">
<title>Cozy Sprouts Business Card</title>
<link rel="stylesheet" href="https://fonts.googleapis.com/css2?family=Comic+Neue:wght@400;700&family=Didact+Gothic&display=swap">
<style>
  :root {
    --page: #ececec;
    --card: #fbfbfb;
    --ink: #1c1c1c;
    --orange: #e2603a;
    --orange-soft: #e86d45;
    --black: #111111;
    --name-tint: #f6cdbd;
    --title-tint: #f2b9a3;
    --line: #d8d8d8;
  }
  * { margin: 0; padding: 0; box-sizing: border-box; }
  html, body { width: 1200px; height: 970px; overflow: hidden; background: var(--page); }
  .canvas { position: relative; width: 1200px; height: 970px; }
  .card {
    position: absolute; left: 80px; top: 195px; width: 1040px; height: 580px;
    background: var(--card); border: 1px solid var(--line);
    font-family: "Didact Gothic", "Century Gothic", sans-serif; color: var(--ink);
  }
  .brand-mark {
    position: absolute; left: 190px; top: 70px; width: 100px; height: 100px;
    background: var(--orange);
  }
  .brand-name {
    position: absolute; left: 50px; top: 222px;
    font-family: "Comic Neue", "Comic Sans MS", cursive; font-weight: 400;
    font-size: 56px; line-height: 1; color: var(--ink);
  }
  .band { position: absolute; left: 0; top: 310px; width: 100%; height: 93px; display: flex; }
  .band-orange { width: 756px; height: 100%; background: var(--orange-soft); }
  .band-black { flex: 1; height: 100%; background: var(--black); display: flex; align-items: center; padding-left: 40px; }
  .band-brand { font-family: "Comic Neue", "Comic Sans MS", cursive; font-size: 30px; color: #ffffff; }
  .person { position: absolute; left: 50px; top: 325px; }
  .person-name { font-size: 29px; font-weight: 700; color: var(--name-tint); line-height: 1.2; }
  .person-title { font-size: 24px; color: var(--title-tint); line-height: 1.1; }
  .contacts { position: absolute; left: 50px; top: 440px; list-style: none; }
  .contacts li { display: flex; align-items: center; gap: 10px; font-size: 23px; height: 31px; }
  .contacts svg { width: 18px; height: 18px; flex: none; }
  .address { position: absolute; left: 697px; top: 472px; font-size: 23px; line-height: 31px; }
  .baseline { position: absolute; left: 0; top: 571px; width: 100%; height: 6px; display: flex; }
  .baseline-orange { width: 742px; background: var(--orange); }
  .baseline-black { flex: 1; background: var(--black); }
</style>
</head>
<body>
<div class="canvas">
  <div class="card">
    <div class="brand-mark"></div>
    <div class="brand-name">Cozy Sprouts</div>

    <div class="band">
      <div class="band-orange"></div>
      <div class="band-black"><span class="band-brand">Cozy Sprouts</span></div>
    </div>

    <div class="person">
      <div class="person-name">Rosalind Vantrey</div>
      <div class="person-title">Ceo</div>
    </div>

    <ul class="contacts">
      <li>
        <svg viewBox="0 0 20 20" aria-hidden="true"><path d="M4 2 L8 2 L9 6 L6.5 7.5 Q8.5 11.5 12.5 13.5 L14 11 L18 12 L18 16 Q18 18 16 18 Q3 17 2 4 Q2 2 4 2Z" fill="var(--orange)"/></svg>
        5415817320
      </li>
      <li>
        <svg viewBox="0 0 20 20" aria-hidden="true"><rect x="1" y="4" width="18" height="12" fill="var(--orange)"/><path d="M1 4 L10 11 L19 4" stroke="#fff" stroke-width="1.6" fill="none"/></svg>
        Info@Cozy-Sprouts.com
      </li>
      <li>
        <svg viewBox="0 0 20 20" aria-hidden="true"><circle cx="10" cy="10" r="8.5" fill="var(--orange)"/><g stroke="#fff" stroke-width="1.2" fill="none"><ellipse cx="10" cy="10" rx="3.5" ry="8.5"/><line x1="1.5" y1="10" x2="18.5" y2="10"/><line x1="3" y1="6" x2="17" y2="6"/><line x1="3" y1="14" x2="17" y2="14"/></g></svg>
        www.Cozy-Sprouts.com
      </li>
    </ul>

    <div class="address">
      <div>24816 Maplecrest D #5172</div>
      <div>Brenwick Or 97318</div>
    </div>

    <div class="baseline">
      <div class="baseline-orange"></div>
      <div class="baseline-black"></div>
    </div>
  </div>
</div>
</body>
</html>
```